Redesign Digital Lending Mobile App - Android/ Flutter

Want to re-theme an existing Digital Lending Mobile app to simplify customer journeys, as well as uplift the UI.

Most users will have small screen phones so the design needs to take that into consideration while also adapting to those with larger devices, like admins with Tablets.

Have already laid out customer journeys on Figma with guidance on how the flow of the app should be. https://www.plandeck.example/board/q4tRw8KzPmYx2LbNvcHsaT/KovaPay?view-id=3-5120&k=Zu8pRtQwLmNcXbYa-2

Video capture of current app: https://vault.trelmora.example/clip/d/7Hq2WmRtLp9XzKcVbNa4YsDfGe8JuQo3/view
https://vault.trelmora.example/clip/d/4Pn8ZxCvBq1MwLtRyHs6KdJgFa2UeXi9/view

The documented views for Web are also here https://docs.quenlaro.example/open?id=3A8C2D4F6B1E9077!kb2d58e71403a4c6e8f2a91d04b7c3e68&resid=3A8C2D4F6B1E9077!kb2d58e71403a4c6e8f2a91d04b7c3e68&cid=3a8c2d4f6b1e9077&ithint=file%2Cdocx&redeem=bXhZc2RrcVp0TmxhUGVvV2lGcnVHc0JtWWpLdlFhWHpOcHRMZUR3U2JjUmZUeUFnSGxNb1ZpRXVKd0NrRHNYcVBuWmFNYmd5TGVr&migratedtospo=true&wdo=2
Updates

Corvana Market(s)

Kenya, Tanzania, Uganda - Africa

Industry/Entity Type

Fintech

Requirements
Must have
• Responsive for diff screens, esp. in context of smaller screen smartphone
Nice to have
• Thematic components to ensure new views can easily be adapted to these themse

```html
<!DOCTYPE html>
<html lang="en">
<head>
<meta charset="utf-8">
<title>KovaPay – Lending App Screens</title>
<link href="https://fonts.googleapis.com/css2?family=Montserrat:wght@400;500;600;700&family=Roboto:wght@400;500&display=swap" rel="stylesheet">
<style>
:root{
  --canvas:#f2f2f2;
  --ink-dark:#121419;
  --panel:#ffffff;
  --surface:#f3f3f3;
  --brand-blue:#3478c6;
  --brand-green:#48a06a;
  --text:#111111;
  --muted:#8a8a8a;
  --input:#e8e8e8;
  --key:#4a4a4a;
  --key-dark:#2a2a2a;
  --keyboard:#1c1c1c;
}
*{box-sizing:border-box;margin:0;padding:0}
html,body{width:962px;height:1200px;overflow:hidden}
body{background:var(--canvas);font-family:"Montserrat",sans-serif;color:var(--text);position:relative}
.screen{position:absolute;width:208px;height:456px;border-radius:22px;overflow:hidden;background:var(--panel)}
.abs{position:absolute}
.center-x{left:0;right:0;text-align:center}

/* brand */
.brand-dot{width:40px;height:40px;border-radius:50%;background:var(--brand-blue);left:84px}
.brand-name{font-weight:700;font-size:18px;color:var(--brand-blue);letter-spacing:.3px}

/* splash */
.splash{left:105px;top:110px;background:var(--ink-dark)}
.version{top:430px;font-size:7.5px;color:#fff}

/* login */
.login{left:376px;top:110px}
.login .top{left:0;top:0;width:208px;height:230px;background:var(--ink-dark)}
.form-card{left:12px;top:163px;width:185px;height:126px;background:var(--panel);border-radius:3px}
.label{font-size:6px;font-weight:500}
.field{left:9px;width:168px;height:22px;background:var(--input);border:1px solid #ddd;border-radius:3px;font-size:5.5px;color:#bdbdbd;padding:8px 9px}
.link{color:var(--brand-blue)}
.btn{height:25px;border-radius:3px;color:#fff;font-size:8.5px;display:flex;align-items:center;justify-content:center;font-weight:500}
.btn-green{background:var(--brand-green)}
.btn-blue{background:var(--brand-blue)}

/* pin */
.pin{left:647px;top:110px}
.pin-title{top:82px;font-size:8px;font-weight:500}
.pin-boxes{left:15px;top:99px;width:177px;display:flex;justify-content:space-between}
.pin-box{width:21px;height:23px;background:#ececec;border:1px solid #d6d6d6;border-radius:2px;font-family:"Roboto",sans-serif;font-size:17px;text-align:center;line-height:22px}
.keyboard{left:0;top:272px;width:208px;height:184px;background:var(--keyboard);font-family:"Roboto",sans-serif;color:#eee}
.chip{left:76px;top:5px;width:57px;height:16px;border-radius:8px;background:#444;font-size:7.5px;color:#bbb;display:flex;align-items:center;justify-content:center;gap:4px}
.key-row{left:4px;right:4px;display:flex;gap:2.3px;justify-content:center}
.key{width:18.3px;height:24px;border-radius:4px;background:var(--key);font-size:11px;display:flex;align-items:center;justify-content:center}
.key.wide{width:28px;background:var(--key-dark)}
.key.space{width:78px;font-size:7px;color:#ddd}

/* dashboard */
.dash{left:105px;top:630px;background:var(--surface)}
.dash-head{left:0;top:0;width:208px;height:51px;background:var(--ink-dark)}
.dash-title{left:12px;top:30px;color:#fff;font-size:8px;font-weight:600}
.card{left:11.5px;width:185.5px;height:74px;border-radius:2px;color:#fff}
.card-title{left:9px;top:15px;font-size:8px;font-weight:600}
.card-amount{left:10px;top:41px;font-size:15px;font-weight:700}
.card-brand{right:10px;top:15px;font-size:7px;font-weight:600;display:flex;align-items:center;gap:4px}
.brand-chip{width:9px;height:9px;border-radius:50%;background:#fff}
.list-panel{left:11.5px;width:185.5px;background:var(--panel);border-radius:2px}
.tabs{left:9px;top:12px;font-size:6.5px;display:flex;gap:9px;font-weight:600}
.tabs .off{color:#bdbdbd;font-weight:500}
.tx{left:9px;right:9px;height:24px;display:flex;align-items:center}
.tx-icon{width:22px;height:22px;border-radius:50%;flex:none}
.tx-text{margin-left:6px;flex:1;line-height:1.2}
.tx-name{font-size:6.5px;font-weight:600}
.tx-sub{font-size:6px;color:var(--muted)}
.tx-amt{font-size:6.5px;font-weight:600}

/* loan */
.loan{left:376px;top:630px;background:var(--surface)}
.loan .top{left:0;top:0;width:208px;height:157px;background:var(--ink-dark)}
.loan-title{top:37px;font-size:14px;font-weight:600;color:#fff}
.loan-next{top:65px;font-size:7px;font-weight:600;color:var(--brand-blue)}
.loan-amt{top:81px;font-size:14px;font-weight:700;color:#fff}
.due-pill{left:67px;top:103px;width:74px;height:10px;border-radius:5px;background:#3a3d44;color:var(--brand-blue);font-size:5px;font-weight:600;text-align:center;line-height:10px}
.summary{left:12px;top:121px;width:185px;height:37px;background:var(--panel);font-size:6.5px;font-weight:700;text-align:center}
.pay-btn{left:12px;top:158px;width:185px;height:36px;font-size:11px;font-weight:600;border-radius:0}
.section-head{left:12px;right:11px;top:209px;font-size:6.5px;font-weight:600;display:flex;justify-content:space-between}
.inst{left:9px;right:9px;height:26px;display:flex;align-items:center}
.inst-num{width:22px;height:22px;border-radius:50%;background:#e6e6e6;font-size:8.5px;font-weight:700;display:flex;align-items:center;justify-content:center;flex:none}
</style>
</head>
<body>

<!-- Splash -->
<section class="screen splash">
  <div class="abs brand-dot" style="top:194px"></div>
  <div class="abs center-x brand-name" style="top:240px">KovaPay</div>
  <div class="abs center-x version">Version 1.0</div>
</section>

<!-- Login -->
<section class="screen login">
  <div class="abs top"></div>
  <div class="abs brand-dot" style="top:40px"></div>
  <div class="abs center-x brand-name" style="top:86px">KovaPay</div>
  <div class="abs form-card">
    <div class="abs label" style="left:9px;top:21px">UserName or Email:</div>
    <div class="abs field" style="top:33px">Enter UserName or Email</div>
    <div class="abs label" style="left:9px;top:60px">Password:</div>
    <div class="abs field" style="top:72px">Enter Password</div>
    <div class="abs label link" style="right:9px;top:98px;font-size:5.5px">Forgot Password?</div>
  </div>
  <div class="abs btn btn-green" style="left:12px;top:297px;width:185px">Login</div>
  <div class="abs center-x" style="top:433px;font-size:6.5px;font-weight:500">Not have account: <span class="link">Register Now</span></div>
</section>

<!-- PIN -->
<section class="screen pin">
  <div class="abs center-x pin-title">Enter Your Pin</div>
  <div class="abs pin-boxes">
    <div class="pin-box">7</div><div class="pin-box">9</div><div class="pin-box">7</div>
    <div class="pin-box">0</div><div class="pin-box">9</div><div class="pin-box">3</div>
  </div>
  <div class="abs btn btn-green" style="left:15px;top:131px;width:177px;height:24px;font-size:8px">Submit</div>
  <div class="abs keyboard">
    <div class="abs chip">
      <svg width="8" height="9" viewBox="0 0 8 9"><rect x="1" y="1.5" width="6" height="7" rx="1" fill="none" stroke="#3d8ee0"/><rect x="2.5" y=".5" width="3" height="2" fill="#3d8ee0"/></svg>797093
    </div>
    <div class="abs key-row" style="top:30px">
      <div class="key">q</div><div class="key">w</div><div class="key">e</div><div class="key">r</div><div class="key">t</div><div class="key">y</div><div class="key">u</div><div class="key">i</div><div class="key">o</div><div class="key">p</div>
    </div>
    <div class="abs key-row" style="top:60px">
      <div class="key">a</div><div class="key">s</div><div class="key">d</div><div class="key">f</div><div class="key">g</div><div class="key">h</div><div class="key">j</div><div class="key">k</div><div class="key">l</div>
    </div>
    <div class="abs key-row" style="top:91px">
      <div class="key wide"><svg width="10" height="10" viewBox="0 0 10 10"><path d="M5 1 L9 5 H6.5 V9 H3.5 V5 H1 Z" fill="none" stroke="#eee" stroke-width=".9"/></svg></div>
      <div class="key">z</div><div class="key">x</div><div class="key">c</div><div class="key">v</div><div class="key">b</div><div class="key">n</div><div class="key">m</div>
      <div class="key wide"><svg width="12" height="9" viewBox="0 0 12 9"><path d="M4 1 H11 V8 H4 L1 4.5 Z M6 3 L9 6 M9 3 L6 6" fill="none" stroke="#eee" stroke-width=".9"/></svg></div>
    </div>
    <div class="abs key-row" style="top:122px">
      <div class="key wide" style="font-size:7.5px">?123</div>
      <div class="key wide" style="width:20px">☺</div>
      <div class="key wide" style="width:18px">,</div>
      <div class="key space">English (USA)</div>
      <div class="key wide" style="width:18px">.</div>
      <div class="key wide"><svg width="9" height="9" viewBox="0 0 9 9"><circle cx="3.8" cy="3.8" r="2.8" fill="none" stroke="#3d8ee0" stroke-width="1"/><path d="M5.8 5.8 L8.5 8.5" stroke="#3d8ee0" stroke-width="1"/></svg></div>
    </div>
    <svg class="abs" style="left:16px;top:158px" width="8" height="6" viewBox="0 0 8 6"><path d="M1 1.5 L4 4.5 L7 1.5" fill="none" stroke="#ccc" stroke-width="1"/></svg>
  </div>
</section>

<!-- Dashboard -->
<section class="screen dash">
  <div class="abs dash-head"></div>
  <div class="abs dash-title">Dashboard</div>
  <svg class="abs" style="left:167px;top:29px" width="10" height="11" viewBox="0 0 10 11"><path d="M2 8 V5 a3 3 0 0 1 6 0 V8 L9 9 H1 Z M4 10 h2" fill="none" stroke="#fff" stroke-width=".9"/></svg>
  <svg class="abs" style="left:184px;top:30px" width="11" height="9" viewBox="0 0 11 9"><path d="M1 1 H10 M1 4.5 H10 M1 8 H10" stroke="#fff" stroke-width="1"/></svg>

  <div class="abs card" style="top:72px;background:var(--brand-blue)">
    <div class="abs card-title">Platinum Credit</div>
    <div class="abs card-brand"><span class="brand-chip"></span>Cardlynx</div>
    <div class="abs card-amount">$10,242,91↑</div>
  </div>
  <div class="abs card" style="top:168px;background:var(--brand-green)">
    <div class="abs card-title">Platinum Credit</div>
    <div class="abs card-brand">Paylo</div>
    <div class="abs card-amount">$10,242,91↓</div>
  </div>

  <div class="abs list-panel" style="top:263px;height:165px">
    <div class="abs tabs"><span>Transactions</span><span class="off">Billing</span><span class="off">Upcoming</span></div>
    <svg class="abs" style="right:9px;top:9px" width="13" height="13" viewBox="0 0 13 13"><circle cx="6.5" cy="6.5" r="6.5" fill="#ececec"/><path d="M4 9 L9 4 M6.5 4 H9 V6.5 M4 6.5 V9 H6.5" fill="none" stroke="#333" stroke-width=".8"/></svg>
    <div class="abs tx" style="top:32px"><div class="tx-icon" style="background:#d8192a"></div><div class="tx-text"><div class="tx-name">Corvana</div><div class="tx-sub">Groceries</div></div><div class="tx-amt">-$99,99</div></div>
    <div class="abs tx" style="top:66px"><div class="tx-icon" style="background:#2a8fd6"></div><div class="tx-text"><div class="tx-name">Telvia</div><div class="tx-sub">Monthly Data Charges</div></div><div class="tx-amt">-$99,99</div></div>
    <div class="abs tx" style="top:99px"><div class="tx-icon" style="background:#e9e9e9"></div><div class="tx-text"><div class="tx-name">Parcelo Plus</div><div class="tx-sub">Paid on January 2024</div></div><div class="tx-amt">-$99,99</div></div>
    <div class="abs tx" style="top:133px"><div class="tx-icon" style="background:#1a1a1a"></div><div class="tx-text"><div class="tx-name">Streamora</div><div class="tx-sub">Paid on January 2024</div></div><div class="tx-amt">-$99,99</div></div>
  </div>
</section>

<!-- Loan details -->
<section class="screen loan">
  <div class="abs top"></div>
  <div class="abs center-x loan-title">Loan Details</div>
  <div class="abs center-x loan-next">Next Repayment</div>
  <div class="abs center-x loan-amt">$99,99</div>
  <div class="abs due-pill">On December 2024</div>
  <div class="abs summary">
    <div class="abs" style="left:10px;top:8px">Paid Amount<br>$99,99</div>
    <div class="abs" style="right:10px;top:8px">Remaining Payment<br>$99,99</div>
  </div>
  <div class="abs btn btn-blue pay-btn">Pay Installments</div>
  <div class="abs section-head"><span>Installments</span><span>Repayment</span></div>
  <div class="abs list-panel" style="top:222px;height:206px">
    <div class="abs inst" style="top:5px"><div class="inst-num">1</div><div class="tx-text"><div class="tx-name">Tenor 1</div><div class="tx-sub">Paid on January 2024</div></div><div class="tx-amt">$99,99</div></div>
    <div class="abs inst" style="top:39px"><div class="inst-num">2</div><div class="tx-text"><div class="tx-name">Tenor 2</div><div class="tx-sub">Paid on January 2024</div></div><div class="tx-amt">$99,99</div></div>
    <div class="abs inst" style="top:73px"><div class="inst-num">3</div><div class="tx-text"><div class="tx-name">Tenor 3</div><div class="tx-sub">Paid on January 2024</div></div><div class="tx-amt">$99,99</div></div>
    <div class="abs inst" style="top:106px"><div class="inst-num">4</div><div class="tx-text"><div class="tx-name">Tenor 4</div><div class="tx-sub">Paid on January 2024</div></div><div class="tx-amt">$99,99</div></div>
    <div class="abs inst" style="top:139px"><div class="inst-num">5</div><div class="tx-text"><div class="tx-name">Tenor 5</div><div class="tx-sub">Paid on January 2024</div></div><div class="tx-amt">$99,99</div></div>
    <div class="abs inst" style="top:171px"><div class="inst-num">6</div><div class="tx-text"><div class="tx-name">Tenor 6</div><div class="tx-sub">Paid on January 2024</div></div><div class="tx-amt">$99,99</div></div>
  </div>
</section>

</body>
</html>
```